Business Card Design

i am looking a business card for a car rental company long with Taxi service also a logo.

what is the latest with my project

Industry/Entity Type

Business

Contact Information for Business Card

name of the Company is Kestrel Bay Motor Leasing and Taxi Services
Address: Harrow Point Village, St. Brennan's Parish Antigua
Tele# 555-0142/5550187-555-0163
Email: lorimbeck@quillmarsh.test

Font styles to use
Script

```html
<!DOCTYPE html>
<html lang="en">
<head>
<meta charset="utf-8">
<title>Kestrel Bay Motor Leasing and Taxi Services – Business Card</title>
<link rel="stylesheet" href="https://fonts.googleapis.com/css2?family=Noto+Serif:wght@400;700&display=swap">
<style>
  :root {
    --backdrop: #7d5f40;
    --taxi-yellow: #f1d52b;
    --yellow-light: #f7e461;
    --yellow-deep: #e2c21c;
    --asphalt-dark: #2b2c2d;
    --asphalt-mid: #5a5b5a;
    --band-black: #1c1d1e;
    --ink: #2a2a26;
    --ink-soft: #4b4a40;
  }
  html, body {
    margin: 0;
    width: 1200px;
    height: 1023px;
    overflow: hidden;
    background: var(--backdrop);
  }
  .business-card {
    position: absolute;
    left: 100px;
    top: 226px;
    width: 1000px;
    height: 571px;
    box-shadow: 0 18px 40px rgba(0,0,0,0.45);
  }
  .business-card svg { display: block; }
  .company-name {
    font-family: "Noto Serif", Georgia, serif;
    font-weight: 700;
    font-size: 52px;
    fill: var(--taxi-yellow);
  }
  .person-name {
    font-family: "Noto Serif", Georgia, serif;
    font-weight: 700;
    font-size: 34px;
    fill: var(--ink);
  }
  .person-role {
    font-family: "Noto Serif", Georgia, serif;
    font-size: 20px;
    fill: var(--ink-soft);
  }
  .contact-line {
    font-family: "Noto Serif", Georgia, serif;
    font-size: 21px;
    fill: var(--ink);
  }
  .address-line {
    font-family: "Noto Serif", Georgia, serif;
    font-size: 22px;
    fill: var(--taxi-yellow);
  }
  .contact-icon { fill: var(--ink); }
  .contact-icon-mark { stroke: var(--taxi-yellow); stroke-width: 1.6; fill: none; }
</style>
</head>
<body>
<div class="business-card">
  <svg width="1000" height="571" viewBox="0 0 1000 571" xmlns="http://www.w3.org/2000/svg">
    <defs>
      <clipPath id="card-shape"><rect width="1000" height="571"/></clipPath>
      <linearGradient id="asphalt-tone" x1="0" y1="0" x2="1" y2="1">
        <stop offset="0" stop-color="var(--asphalt-mid)"/>
        <stop offset="0.5" stop-color="var(--asphalt-dark)"/>
        <stop offset="1" stop-color="var(--asphalt-mid)"/>
      </linearGradient>
      <linearGradient id="yellow-sheen" x1="0" y1="0" x2="0" y2="1">
        <stop offset="0" stop-color="var(--yellow-light)"/>
        <stop offset="1" stop-color="var(--yellow-deep)"/>
      </linearGradient>
    </defs>
    <g clip-path="url(#card-shape)">
      <g transform="rotate(-5.71)">
        <rect class="road-photo" role="img" aria-label="Photo of an asphalt road with white lane markings" x="-200" y="-300" width="1500" height="558" fill="url(#asphalt-tone)"/>
        <rect class="edge-line" x="-200" y="256" width="1500" height="4" fill="var(--taxi-yellow)"/>
        <rect class="dark-stripe" x="-200" y="260" width="1500" height="12" fill="var(--band-black)"/>
        <rect class="yellow-band" x="-200" y="272" width="1500" height="186" fill="url(#yellow-sheen)"/>
        <rect class="address-band" x="-200" y="458" width="1500" height="400" fill="var(--band-black)"/>

        <text class="company-name" x="80" y="150">Kestrel Bay Motor</text>
        <text class="company-name" x="80" y="218">Leasing and Taxi Services</text>

        <g class="contact-block">
          <text class="contact-line" x="895" y="318" text-anchor="end">555-0142-555-0163</text>
          <rect class="contact-icon" x="906" y="302" width="18" height="18" rx="3"/>
          <path class="contact-icon-mark" d="M910 306 q0 9 9 10"/>
          <text class="contact-line" x="895" y="352" text-anchor="end">555-0187-555-0163</text>
          <rect class="contact-icon" x="906" y="336" width="18" height="18" rx="3"/>
          <path class="contact-icon-mark" d="M910 340 q0 9 9 10"/>
          <text class="contact-line" x="895" y="386" text-anchor="end">lorimbeck@quillmarsh.test</text>
          <rect class="contact-icon" x="906" y="370" width="18" height="18" rx="3"/>
          <path class="contact-icon-mark" d="M910 375 h10 v8 h-10 z M910 375 l5 4 l5 -4"/>
        </g>

        <text class="person-name" x="80" y="410">Dorian Wellaby</text>
        <text class="person-role" x="82" y="438">Director</text>

        <text class="address-line" x="80" y="508">Harrow Point Village, St. Brennan's Parish Antigua</text>
      </g>
    </g>
  </svg>
</div>
</body>
</html>
```